Town Planning Consultants require lstationary design

Require a design to be used for our letterhead and report cover page. We have an approved logo.
we have attached our logo, and our temporary letterhead/cover page (SEE Cover) which we currently adapt for both purposes in the interim pending a permanent design. I have also attached an example (example report cover) of a report cover page that I like. perhaps similar with our colour scheme

Target Market(s)

?

Industry/Entity Type

Town

Colors
249fd4
3176b5

Requirements
Must have
• colours to match logo
• the text content in existing letterhead

```html
<!DOCTYPE html>
<html lang="en">
<head>
<meta charset="utf-8">
<title>Kestrel Urban Stationery</title>
<link rel="stylesheet" href="https://fonts.googleapis.com/css2?family=Lato:wght@400;700&family=Arimo:wght@400;700&family=Oswald:wght@600&display=swap">
<style>
  :root {
    --bg: #c4c4c4;
    --paper: #ffffff;
    --brand: #5b9bd3;
    --brand-deep: #4d76b3;
    --ink: #222222;
    --muted: #6e6e6e;
    --rule: #9cc2e6;
    --soft: #a9cdee;
  }
  * { box-sizing: border-box; margin: 0; padding: 0; }
  html, body { width: 1200px; height: 1200px; overflow: hidden; }
  body { background: var(--bg); position: relative; font-family: "Arimo", Arial, sans-serif; color: var(--ink); }

  .sheet { position: absolute; background: var(--paper); box-shadow: 0 1px 3px rgba(0,0,0,.25); overflow: hidden; }

  .wordmark { font-family: "Lato", Arial, sans-serif; font-weight: 400; color: var(--brand); white-space: nowrap; display: flex; align-items: center; }
  .wordmark .mark { display: inline-block; background: currentColor; margin-right: .35em; width: .55em; height: .55em; }

  /* business card front */
  .card-front { left: 137px; top: 115px; width: 268px; height: 148px; }
  .card-front .wordmark { position: absolute; left: 32px; top: 66px; font-size: 15px; }
  .card-front .divider { position: absolute; left: 129px; top: 33px; height: 82px; border-left: 1px dotted #888; }
  .card-front .name { position: absolute; left: 139px; top: 33px; font-size: 12px; color: var(--brand); }
  .card-front .role { position: absolute; left: 139px; top: 48px; font-size: 8.5px; color: var(--muted); }
  .card-front .contacts { position: absolute; left: 139px; top: 66px; list-style: none; font-size: 6.3px; line-height: 9.6px; color: #444; }
  .card-front .contacts li { display: flex; gap: 4px; }
  .icon { width: 6px; height: 7px; flex: none; margin-top: 1px; }
  .card-front .band { position: absolute; left: 0; bottom: 0; width: 100%; height: 7px; background: var(--brand); }

  /* business card back */
  .card-back { left: 137px; top: 282px; width: 270px; height: 148px; background: var(--brand); }
  .card-back .wordmark { position: absolute; left: 0; right: 0; top: 52px; justify-content: center; font-size: 34px; color: #fff; }

  /* envelope */
  .envelope { left: 627px; top: 139px; width: 496px; height: 251px; }
  .envelope .wordmark { position: absolute; left: 26px; top: 54px; font-size: 24px; }
  .envelope .return { position: absolute; left: 30px; top: 205px; padding-left: 10px; border-left: 1px solid var(--brand); font-size: 8.5px; line-height: 11px; }

  /* letterhead */
  .letterhead { left: 137px; top: 459px; width: 439px; height: 621px; }
  .letterhead .wordmark { position: absolute; left: 40px; top: 50px; font-size: 27px; }
  .letterhead .contacts { position: absolute; left: 324px; top: 42px; list-style: none; font-size: 6.5px; line-height: 11px; }
  .letterhead .contacts li { display: flex; gap: 4px; }
  .letterhead .address { position: absolute; left: 40px; top: 141px; font-size: 6.5px; line-height: 10px; }
  .letter-body { position: absolute; left: 40px; top: 207px; width: 345px; font-size: 6.4px; line-height: 10.2px; }
  .letter-body .salute { font-size: 8px; margin-bottom: 8px; }
  .letter-body p { margin-bottom: 10px; }
  .letter-body .closing { font-size: 7px; margin-top: 12px; }
  .signature { display: block; width: 64px; height: 28px; margin: 6px 0 8px; background: linear-gradient(90deg, rgba(91,155,211,.35), rgba(91,155,211,.1)); }
  .letter-body .signer { font-size: 7px; line-height: 10px; }
  .letter-body .signer strong { display: block; }
  .letterhead .services { position: absolute; left: 107px; top: 578px; font-size: 7.4px; color: var(--brand); display: flex; }
  .letterhead .services span + span { border-left: 1px solid var(--brand); margin-left: 3px; padding-left: 3px; }

  /* report cover */
  .report { left: 635px; top: 459px; width: 435px; height: 614px; }
  .report .wordmark { position: absolute; left: 0; right: 0; top: 72px; justify-content: center; font-size: 28px; }
  .report .shapes { position: absolute; left: 0; top: 0; }
  .report .eyebrow { position: absolute; left: 48px; top: 270px; font-size: 7.6px; font-weight: 700; letter-spacing: .2px; color: #1f2d44; }
  .report .title { position: absolute; left: 48px; top: 284px; font-family: "Oswald", "Arial Narrow", sans-serif; font-weight: 600; font-size: 21px; line-height: 25px; color: #fff; letter-spacing: -.4px; }
  .report .subtitle { position: absolute; left: 48px; top: 380px; font-size: 17px; color: #2a3442; }
  .report .rule { position: absolute; left: 48px; top: 419px; width: 342px; border-top: 1px solid var(--soft); }
  .report .site { position: absolute; left: 48px; top: 431px; font-size: 8px; font-weight: 700; color: #1f2d44; }
  .report .date { position: absolute; right: 31px; top: 576px; font-size: 10px; color: var(--soft); }
</style>
</head>
<body>

<section class="sheet card-front" aria-label="Business card front">
  <div class="wordmark"><span class="mark"></span>Kestrel Urban</div>
  <div class="divider"></div>
  <div class="name">M.Hale</div>
  <div class="role">Owner</div>
  <ul class="contacts">
    <li><svg class="icon" viewBox="0 0 6 7"><path d="M3 0a2.3 2.3 0 0 0-2.3 2.3C.7 4 3 7 3 7s2.3-3 2.3-4.7A2.3 2.3 0 0 0 3 0zm0 3.2a.9.9 0 1 1 0-1.8.9.9 0 0 1 0 1.8z" fill="#5b9bd3"/></svg><span>12 Harbour Ridge Road,<br>ALDERVALE NSW 2400</span></li>
    <li><svg class="icon" viewBox="0 0 6 7"><path d="M1 .5l1.3 1.6-.6.8c.4.9 1 1.6 1.9 2l.8-.6L6 5.6 5 6.6C2.5 6 .3 3.7 0 1.4z" fill="#5b9bd3"/></svg><span>+61 (2) 5550 1234</span></li>
    <li><svg class="icon" viewBox="0 0 6 7"><rect x="1.2" y=".3" width="3.6" height="6.4" rx=".6" fill="none" stroke="#5b9bd3" stroke-width=".8"/></svg><span>+61 (0)400 555 018</span></li>
    <li><svg class="icon" viewBox="0 0 6 7"><rect x=".3" y="1.8" width="5.4" height="3.6" fill="#5b9bd3"/></svg><span>mia@kestrelurban.com.au</span></li>
  </ul>
  <div class="band"></div>
</section>

<section class="sheet card-back" aria-label="Business card back">
  <div class="wordmark"><span class="mark"></span>Kestrel Urban</div>
</section>

<section class="sheet envelope" aria-label="Envelope">
  <div class="wordmark"><span class="mark"></span>Kestrel Urban</div>
  <div class="return">12 Harbour Ridge Road,<br>ALDERVALE NSW 2400</div>
</section>

<section class="sheet letterhead" aria-label="Letterhead">
  <div class="wordmark"><span class="mark"></span>Kestrel Urban</div>
  <ul class="contacts">
    <li><svg class="icon" viewBox="0 0 6 7"><path d="M1 .5l1.3 1.6-.6.8c.4.9 1 1.6 1.9 2l.8-.6L6 5.6 5 6.6C2.5 6 .3 3.7 0 1.4z" fill="#5b9bd3"/></svg><span>+61 (2) 5550 1234</span></li>
    <li><svg class="icon" viewBox="0 0 6 7"><rect x="1.2" y=".3" width="3.6" height="6.4" rx=".6" fill="none" stroke="#5b9bd3" stroke-width=".8"/></svg><span>+61 (0)400 555 018</span></li>
    <li><svg class="icon" viewBox="0 0 6 7"><rect x=".3" y="1.8" width="5.4" height="3.6" fill="#5b9bd3"/></svg><span>mia@kestrelurban.com.au</span></li>
  </ul>
  <div class="address">12 Harbour Ridge Road,<br>ALDERVALE NSW 2400</div>
  <div class="letter-body">
    <div class="salute">Dear Sir.</div>
    <p>Lorem ipsum. Proin gravida nibh vel velit auctor aliquet. Aenean sollicitudin, lorem quis bibendum auctor, nisi elit consequat ipsum, nec sagittis sem nibh id elit. Duis sed odio sit amet nibh vulputate cursus a sit amet mauris. Morbi accumsan ipsum velit. Nam nec tellus a odio tincidunt auctor a ornare odio. Sed non mauris vitae erat consequat auctor eu in elit.</p>
    <p>Class aptent taciti sociosqu ad litora torquent per conubia nostra, per inceptos himenaeos. Mauris in erat justo. Nullam ac urna eu felis dapibus condimentum sit amet a augue. Sed non neque elit. Sed ut imperdiet nisi. Proin condimentum fermentum nunc. Etiam pharetra, erat sed fermentum feugiat, velit mauris egestas quam, ut aliquam massa nisl quis neque. Suspendisse in orci enim.</p>
    <p>Lorem ipsum. Proin gravida nibh vel velit auctor aliquet. Aenean sollicitudin, lorem quis bibendum auctor, nisi elit consequat ipsum, nec sagittis sem nibh id elit. Duis sed odio sit amet nibh vulputate cursus a sit amet mauris. Morbi accumsan ipsum velit. Nam nec tellus a odio tincidunt auctor a ornare odio. Sed non mauris vitae erat consequat auctor eu in elit. fermentum feugiat, velit mauris egestas quam, ut aliquam massa nisl quis neque. Suspendisse in orci enim.</p>
    <div class="closing">Kind Regards,</div>
    <span class="signature" role="img" aria-label="Handwritten signature"></span>
    <div class="signer"><strong>M.Hale</strong>Owner and Principal</div>
  </div>
  <div class="services"><span>PLANNING</span><span>DEVELOPMENT</span><span>URBAN DESIGN</span><span>CONSULTANTS</span></div>
</section>

<section class="sheet report" aria-label="Report cover">
  <svg class="shapes" width="435" height="614" viewBox="0 0 435 614">
    <polygon points="0,203 435,258 435,515 0,606" fill="#5b9bd3"/>
    <polygon points="137,219 435,173 435,258" fill="#4d76b3"/>
  </svg>
  <div class="wordmark"><span class="mark"></span>Kestrel Urban</div>
  <div class="eyebrow">DEVELOPMENT APPLICATION</div>
  <div class="title">STATEMENT OF<br>ENVIRONMENTAL EFFECTS</div>
  <div class="subtitle">Proposed Additions to Existing Dwelling</div>
  <div class="rule"></div>
  <div class="site">9 Linden Avenue, MAPLE HILL</div>
  <div class="date">JUNE, 2016</div>
</section>

</body>
</html>
```